Graphic Design for Korrumbyn Animal Hospital

We are a veterinary clinic. Our work is a mixture of dogs, cats mainly but we also do horses, cattle, sheep, goats, alpaca and some birds.

```html
<!DOCTYPE html>
<html lang="en">
<head>
<meta charset="utf-8">
<title>Korrumbyn Animal Hospital</title>
<link rel="stylesheet" href="https://fonts.googleapis.com/css2?family=Merriweather:wght@700;900&display=swap">
<style>
  :root {
    --ink-navy: #2a3f93;
    --ink-sky: #2f93d3;
    --ink-deep: #1d2670;
    --ink-black: #111111;
    --band-blue: #3f60aa;
    --band-edge: #33508f;
    --cream: #f4ea8c;
    --white: #ffffff;
    --sun: #ffd84a;
    --orange: #f0773a;
    --magenta: #e8359a;
    --art-blue: #3a4fae;
    --art-pale: #eef0f7;
  }
  * { margin: 0; padding: 0; box-sizing: border-box; }
  html, body {
    width: 1200px;
    height: 476px;
    overflow: hidden;
    background: var(--white);
  }
  .card {
    position: relative;
    width: 1200px;
    height: 476px;
    font-family: "Merriweather", Georgia, serif;
    font-weight: 700;
  }
  .clinic-name {
    position: absolute;
    left: 97px;
    top: 2px;
    font-size: 48px;
    font-weight: 900;
    letter-spacing: 1px;
    white-space: nowrap;
    color: var(--ink-navy);
  }
  .clinic-name .accent { color: var(--ink-sky); }
  .tagline {
    position: absolute;
    left: 164px;
    top: 56px;
    font-size: 27px;
    color: var(--ink-deep);
    white-space: nowrap;
  }
  .vet-name {
    position: absolute;
    top: 100px;
    font-size: 24px;
    color: var(--ink-black);
    white-space: nowrap;
  }
  .vet-name--left { left: 42px; }
  .vet-name--right { left: 600px; }
  .swatch {
    position: absolute;
    top: 137px;
    height: 130px;
  }
  .swatch--left {
    left: 0;
    width: 196px;
    background: linear-gradient(90deg, var(--sun) 0%, var(--orange) 50%, var(--magenta) 100%);
  }
  .swatch--right {
    left: 694px;
    width: 198px;
    background: linear-gradient(90deg, var(--magenta) 0%, var(--orange) 50%, var(--sun) 100%);
  }
  .mascot-art {
    position: absolute;
    left: 259px;
    top: 108px;
    width: 326px;
    height: 150px;
    background: linear-gradient(90deg, var(--art-blue) 0%, var(--art-blue) 35%, var(--art-pale) 70%, var(--white) 100%);
    border-radius: 40px;
  }
  .contact-band {
    position: absolute;
    left: 0;
    top: 275px;
    width: 895px;
    height: 152px;
    background: var(--band-blue);
    border: 2px solid var(--band-edge);
  }
  .address {
    position: absolute;
    left: 34px;
    top: 12px;
    font-size: 35px;
    color: var(--white);
    white-space: nowrap;
  }
  .phone {
    position: absolute;
    right: 27px;
    top: 30px;
    font-size: 48px;
    color: var(--cream);
    white-space: nowrap;
  }
  .website {
    position: absolute;
    right: 24px;
    top: 100px;
    font-size: 26px;
    color: var(--white);
    white-space: nowrap;
  }
</style>
</head>
<body>
  <main class="card">
    <h1 class="clinic-name">Korrumbyn <span class="accent">Animal Hospital</span></h1>
    <p class="tagline">veterinary clinic for pets and livestock</p>

    <p class="vet-name vet-name--left">Dr. Marcus Telford</p>
    <p class="vet-name vet-name--right">Dr. Helena Varga</p>

    <div class="swatch swatch--left"></div>
    <div class="mascot-art" role="img" aria-label="Illustration of a blue dog and a white cat side by side"></div>
    <div class="swatch swatch--right"></div>

    <section class="contact-band">
      <p class="address">14 Lindsay St, Korrumbyn</p>
      <p class="phone">call: 5190 3870</p>
      <p class="website">www.korrumbynanimalhospital.com.au</p>
    </section>
  </main>
</body>
</html>
```